Giving Porter

Need home page design for new website. The winner will have the opportunity to design the entire site.

I have attached 3 files.

1) Sort of a site map. PLEASE do not design the home page based on this wire frame. Be creative and use your expertise.

2) Tagline and Copy for the home page. Please just greek in or make up copy for areas that do not have copy at this time.

3) The logo.
Updates

Hi everyone, I am sorry for the delay. I have been out of town on unexpected business. I will make a decision this week. Thank you all for the great designs. Dale

Industry/Entity Type

Charity

```html
<!DOCTYPE html>
<html lang="en">
<head>
<meta charset="utf-8">
<title>Giving Porter – Home</title>
<link href="https://fonts.googleapis.com/css2?family=Archivo+Narrow:wght@400;600&family=Archivo+Black&family=Open+Sans:ital,wght@0,400;0,600;1,600&display=swap" rel="stylesheet">
<style>
:root{
  --green:#39a843;
  --blue:#1b6a94;
  --navy:#0f3f5a;
  --paper:#f3f2ec;
  --text:#555;
  --dark:#222;
}
*{margin:0;padding:0;box-sizing:border-box}
html,body{width:801px;height:1200px;overflow:hidden}
body{position:relative;background:var(--paper);font-family:"Open Sans",sans-serif;color:var(--text)}
.abs{position:absolute}
.cond{font-family:"Archivo Narrow",sans-serif}

/* header */
.site-header{left:0;top:0;width:801px;height:84px;background:#fff}
.brand{left:69px;top:22px;display:flex;align-items:center;gap:8px;font-size:22px;color:var(--green);font-family:"Open Sans",sans-serif}
.brand-dot{width:26px;height:26px;border-radius:50%;background:var(--blue)}
.social{right:69px;top:12px;display:flex;gap:3px}
.social span{width:18px;height:18px;background:#ccc}
.social span:first-child{background:var(--blue)}
.nav{left:311px;top:47px;display:flex;gap:21px;font-size:14px;color:var(--dark)}
.nav .active{color:var(--blue);position:relative}
.nav .active::before,.nav .active::after{content:"";position:absolute;top:-3px;width:5px;height:24px;border:2px solid var(--green);border-radius:50%}
.nav .active::before{left:-12px;border-right:none}
.nav .active::after{right:-12px;border-left:none}

/* hero */
.hero{left:0;top:84px;width:801px;height:385px;background:linear-gradient(90deg,#c8c8c5,#e6e6e2 55%,#dcdcd8)}
.hero-photo{left:64px;top:84px;width:410px;height:385px;background:linear-gradient(180deg,#8f8f8d,#5e5e5c 60%,#7a7a78)}
.hero-title{right:101px;top:120px;text-align:right;font-family:"Archivo Black",sans-serif;line-height:1;font-weight:400}
.hero-title .l1{font-size:44px;color:var(--green)}
.hero-title .l2{font-size:27px;color:var(--navy);margin-top:12px}
.hero-title .l3{font-size:31px;color:#2f7f2a;margin-top:9px}
.hero-sub{right:101px;top:288px;text-align:right;font-size:16px;color:var(--dark);line-height:22px}
.btn{top:347px;height:26px;color:#fff;font-family:"Archivo Narrow",sans-serif;font-size:15px;font-weight:600;display:flex;align-items:center;justify-content:center}
.btn-demo{left:494px;width:66px;background:var(--green)}
.btn-try{left:570px;width:112px;background:var(--blue)}

/* welcome */
.welcome-title{left:0;width:801px;top:490px;text-align:center;font-size:22px;color:var(--green)}
.welcome-title b{color:var(--blue);font-weight:600}
.rule{left:345px;top:525px;width:110px;height:2px;background:#b9b5a6}
.welcome-copy{left:56px;width:689px;top:536px;text-align:center;font-size:12px;line-height:18.5px;letter-spacing:-0.1px}
.more{left:388px;top:618px}

/* projects */
.projects{left:0;top:662px;width:801px;height:202px;background:linear-gradient(180deg,#d9d6ca,#e7dcc2 50%,#efe8d6)}
.section-title{font-family:"Archivo Narrow",sans-serif;font-size:16px;color:var(--blue)}
.card{top:710px;width:206px;height:130px;overflow:hidden}
.card .img{width:100%;height:100%}
.card .cap{position:absolute;left:0;bottom:0;width:100%;height:26px;background:rgba(27,106,148,.9);color:#fff;font-family:"Archivo Narrow",sans-serif;font-size:16px;line-height:26px;padding-left:12px}

/* testimonials */
.quote-box{left:69px;top:907px;width:279px;height:91px;border:1px dashed #999;padding:10px 18px;text-align:center;font-size:9.6px;line-height:17px;color:#555}
.avatar{left:180px;top:977px;width:57px;height:48px;background:linear-gradient(135deg,#cfe0ea,#9fb7c6)}
.person{left:69px;width:279px;text-align:center}

/* events */
.event{width:111px}
.event .img{width:111px;height:82px}
.event h4{font-size:10.2px;font-weight:400;color:var(--blue);margin-top:10px;white-space:nowrap}
.event p{font-size:8.4px;line-height:12px;color:#666;margin-top:3px}
.event time{display:block;font-size:8.6px;color:var(--green);margin-top:7px}

/* tweet */
.tweet-band{left:0;top:1100px;width:801px;height:66px;background:#fff}
.tweet-badge{left:372px;top:1076px;width:57px;height:57px;border-radius:50%;background:#fff}
.tweet-badge i{position:absolute;left:18px;top:16px;width:20px;height:20px;border-radius:50%;background:var(--blue)}
.tweet-meta{left:0;width:801px;top:1112px;text-align:center;font-size:11px;color:var(--dark)}
.tweet-meta a{color:var(--blue);font-weight:600;text-decoration:none;margin-right:30px}
.tweet-text{left:0;width:801px;top:1135px;text-align:center;font-size:10px;color:var(--dark)}
.tweet-text span{color:var(--blue)}

/* footer */
.site-footer{left:0;top:1166px;width:801px;height:34px;background:var(--blue);color:#d9e8f0;font-size:8.6px}
.site-footer .links{position:absolute;left:69px;top:11px}
.site-footer .links b{color:#fff;font-weight:400}
.site-footer .copy{position:absolute;right:69px;top:11px}
</style>
</head>
<body>

<header class="abs site-header"></header>
<div class="abs brand"><span class="brand-dot"></span>GivingPorter.com</div>
<div class="abs social"><span></span><span></span><span></span><span></span><span></span></div>
<nav class="abs nav cond">
  <span class="active">Home</span><span>About Us</span><span>Pricing</span><span>Features</span><span>Services</span><span>Products</span><span>Contact Us</span>
</nav>

<section class="abs hero"></section>
<div class="abs hero-photo" role="img" aria-label="Black and white photo of three smiling children"></div>
<svg class="abs" style="left:36px;top:245px" width="22" height="62"><polyline points="20,1 2,31 20,61" fill="none" stroke="#777" stroke-width="1.5"/></svg>
<svg class="abs" style="left:743px;top:245px" width="22" height="62"><polyline points="2,1 20,31 2,61" fill="none" stroke="var(--blue)" stroke-width="1.5"/></svg>
<h1 class="abs hero-title"><div class="l1">SUCCESSFUL</div><div class="l2">NOT STRESSFUL</div><div class="l3">FUNDRAISING</div></h1>
<p class="abs hero-sub">Charity Success, Minus the Stress<br>Sign Up Today for a Free Trial!</p>
<a class="abs btn btn-demo">DEMO</a>
<a class="abs btn btn-try">TRY FOR FREE</a>

<h2 class="abs welcome-title cond" style="font-weight:400">WELCOME TO <b>GIVING PORTER</b></h2>
<div class="abs rule"></div>
<p class="abs welcome-copy">If you are thinking about having a fundraiser, there is no better and more popular event than charity golf.But the time it takes to create invitations, registrations, banners, graphics, donors, as well as organizing and managing the entire event can be quite off-putting. But don’t put it off – PUTT it off! GivingPorter.com is the helping hand you need to create a great charity golf event that will be stress-free and, most importantly, help you raise money to achieve your goal.</p>
<svg class="abs more" width="25" height="25"><circle cx="12.5" cy="12.5" r="12.5" fill="var(--blue)"/><polyline points="10,7 16,12.5 10,18" fill="none" stroke="#fff" stroke-width="2.5"/></svg>

<section class="abs projects" role="img" aria-label="Soft blurred autumn background"></section>
<h3 class="abs section-title" style="left:0;width:801px;top:678px;text-align:center;font-weight:400">RECENT PROJECTS</h3>
<div class="abs card" style="left:69px"><div class="img" role="img" aria-label="Photo of runners at a charity race" style="background:linear-gradient(160deg,#3d3440,#6b3a3c 50%,#2e3a45)"></div>
  <svg style="position:absolute;left:91px;top:50px" width="24" height="24"><circle cx="12" cy="12" r="12" fill="var(--green)"/><polyline points="10,6 16,12 10,18" fill="none" stroke="#fff" stroke-width="2.5"/></svg>
  <div class="cap">Raise More, Stress Less</div></div>
<div class="abs card" style="left:298px"><div class="img" role="img" aria-label="Photo of two smiling children" style="background:linear-gradient(135deg,#6b4a35,#a67c5a 50%,#5a3b28)"></div><div class="cap">Everything you need</div></div>
<div class="abs card" style="left:526px"><div class="img" role="img" aria-label="Photo of a house with a for-sale sign" style="background:linear-gradient(180deg,#7d9bbd,#8fa6b8 40%,#b9a46a 75%,#6f8a4a)"></div><div class="cap">Sold! Silent Auction Moducle</div></div>

<h3 class="abs section-title" style="left:69px;top:880px;font-weight:400">TESTIMONIALS</h3>
<div class="abs quote-box">“ Lorem ipsum dolor sit amet, consectr adipiscing elit. Cras porta arcu nec orci accumsan tempus. Etiam rit gravida ligula sed condimentum. ”</div>
<div class="abs avatar" role="img" aria-label="Portrait photo of the reviewer"></div>
<div class="abs person" style="top:1028px;font-size:10.5px;font-style:italic;font-weight:600;color:var(--blue)">Marta Lindqvist</div>
<div class="abs person" style="top:1044px;font-size:9.6px;color:#555">Associate director</div>

<h3 class="abs section-title" style="left:388px;top:880px;font-weight:400">SEMINARS AND EVENTS</h3>
<article class="abs event" style="left:388px;top:907px"><div class="img" role="img" aria-label="Photo of golfers at an event" style="background:linear-gradient(180deg,#6aa7d8,#8bb 45%,#3f8a2e)"></div><h4>Lorem ipsum dolor sit</h4><p>consectetur adipiscing elit. Quisque gravida</p><time>14.06.2014</time></article>
<article class="abs event" style="left:504px;top:907px"><div class="img" role="img" aria-label="Photo of a group on a golf course" style="background:linear-gradient(180deg,#9bb9d4,#5a7d4a 45%,#3f7a2a)"></div><h4>Lorem ipsum dolor sit</h4><p>consectetur adipiscing elit. Quisque gravida</p><time>14.06.2014</time></article>
<article class="abs event" style="left:621px;top:907px"><div class="img" role="img" aria-label="Photo of a golf club and ball on a tee" style="background:linear-gradient(180deg,#d8d0b8,#9fb56a 50%,#5f8a2a)"></div><h4>Lorem ipsum dolor sit</h4><p>adipiscing elit. Quisque gravida lobortis mollis</p><time>14.06.2014</time></article>

<section class="abs tweet-band"></section>
<div class="abs tweet-badge"><i></i></div>
<div class="abs tweet-meta"><a>@HarlowBrookGrp</a>Thursday 3rd July 2014</div>
<p class="abs tweet-text">Just checked out <span>@FreshCraftShow</span> showcase in Eastgate- good place to unearth a jnr. creative if you need one! <span>http://lnk.example/Qp7Rd2</span></p>

<footer class="abs site-footer">
  <div class="links"><b>Home</b> &nbsp;/&nbsp; About Us &nbsp;/&nbsp; Pricing &nbsp;/&nbsp; Features &nbsp;/&nbsp; Services &nbsp;/&nbsp; Products &nbsp;/&nbsp; Conatct Us</div>
  <div class="copy">©2014 Giving Porter. All rights reserved.</div>
</footer>

</body>
</html>
```